Valbrina Soletti Winery 2023 Label

We are just about to bottle our very first Napa Valley Cabernet Sauvignon and need label ideas

Target Market(s)

Cab drinkers who like Napa California Cabs

Industry/Entity Type

Wine Making

Logo Text

Valbrina Soletti 2023 Napa Estate Grown Cabernet Sauvignon

Requirements
Must have
• Winery Name, year of vintage and Napa Estate Cab
Nice to have
• If using the initials V and S use gold letters on black or red background

```html
<!DOCTYPE html>
<html lang="en">
<head>
<meta charset="utf-8">
<title>Valbrina Soletti 2023 Label</title>
<link rel="stylesheet" href="https://fonts.googleapis.com/css2?family=Cinzel:wght@600;700&display=swap">
<style>
  :root {
    --cream: #f8f1e0;
    --gold: #b5892a;
    --gold-soft: rgba(181, 137, 42, 0.35);
  }
  html, body {
    margin: 0;
    padding: 0;
    width: 1200px;
    height: 1200px;
    overflow: hidden;
    background: var(--cream);
  }
  .label {
    position: relative;
    width: 1200px;
    height: 1200px;
    background: var(--cream);
  }
  .label__frame {
    position: absolute;
    inset: 0;
    width: 1200px;
    height: 1200px;
  }
  .label__frame .frame-outer {
    fill: none;
    stroke: var(--gold);
    stroke-width: 15;
  }
  .label__frame .frame-inner {
    fill: none;
    stroke: var(--gold);
    stroke-width: 4;
  }
  .ornament {
    position: absolute;
    left: 454px;
    width: 292px;
    height: 80px;
    border-radius: 40px;
    background: radial-gradient(ellipse at center, var(--gold-soft) 0%, rgba(181,137,42,0.12) 55%, rgba(181,137,42,0) 75%);
  }
  .ornament--top { top: 350px; }
  .ornament--bottom { top: 768px; }
  .label__text {
    position: absolute;
    left: 0;
    width: 1200px;
    margin: 0;
    text-align: center;
    color: var(--gold);
    font-family: "Cinzel", serif;
    line-height: 1;
    white-space: nowrap;
  }
  .winery-name {
    font-size: 80px;
    font-weight: 700;
    letter-spacing: 1px;
  }
  .winery-name--first { top: 462px; }
  .winery-name--second { top: 538px; }
  .vintage {
    top: 622px;
    font-size: 40px;
    font-weight: 700;
    letter-spacing: 3px;
  }
  .varietal {
    font-size: 28px;
    font-weight: 600;
    letter-spacing: 2.5px;
  }
  .varietal--region { top: 672px; }
  .varietal--grape { top: 704px; }
</style>
</head>
<body>
  <main class="label">
    <svg class="label__frame" viewBox="0 0 1500 1500" aria-hidden="true">
      <path class="frame-outer" d="M350,497 H485 C560,420 650,392 750,392 C850,392 940,420 1015,497 H1150 A82,82 0 0 0 1232,578 V922 A82,82 0 0 0 1150,1003 H1015 C940,1080 850,1108 750,1108 C650,1108 560,1080 485,1003 H350 A82,82 0 0 0 268,922 V578 A82,82 0 0 0 350,497 Z"/>
      <path class="frame-inner" d="M373,523 H498 C570,446 650,412 750,412 C850,412 930,446 1002,523 H1127 A78,78 0 0 0 1205,601 V899 A78,78 0 0 0 1127,977 H1002 C930,1054 850,1088 750,1088 C650,1088 570,1054 498,977 H373 A78,78 0 0 0 295,899 V601 A78,78 0 0 0 373,523 Z"/>
    </svg>

    <div class="ornament ornament--top" role="img" aria-label="Gold scrollwork flourish with a central leaf motif"></div>

    <h1 class="label__text winery-name winery-name--first">VALBRINA</h1>
    <p class="label__text winery-name winery-name--second">SOLETTI</p>
    <p class="label__text vintage">2023</p>
    <p class="label__text varietal varietal--region">NAPA ESTATE GROWN</p>
    <p class="label__text varietal varietal--grape">CABERNET SAUVIGNON</p>

    <div class="ornament ornament--bottom" role="img" aria-label="Gold scrollwork flourish with a central leaf motif, inverted"></div>
  </main>
</body>
</html>
```